CordaMax Packaging, for retail brand of graduation tassels

Retail packaging for graduation tassels. Leave space for a UPC on the back bottom of the template. Design must bleed over edges for printing. Use the attached logo in the packaging. The photo is an example of the packaging, but does not match the template. Please use the shape and dimensions of the template. Please provide all standard file formats. The packaging is not specific to a SKU, it is general.
You can change the color of the logo and add the "TM"

Font styles to use
Other font styles liked:
• See logo

Colors

Designer to choose colors to be used in the design.

Requirements
Must have
• Brand logo, color bleeds on the template
• Include any or all of the following information, either on the back or used as call outs on the packaging.
• "Our tassels are made from the highest quality of polyester available, resulting in accurate and consistent school colors. Each tassel has 50-60 braided yarns. The signets are made from Zinc alloy or solid brass (depending on color)"
Nice to have
• gets the attention of consumers
Should not have
• nothing specific to a SKU

```html
<!DOCTYPE html>
<html lang="en">
<head>
<meta charset="utf-8">
<title>CordaMax Graduation Tassel – Box Template</title>
<link rel="stylesheet" href="https://fonts.googleapis.com/css2?family=Kaushan+Script&family=Playfair+Display:wght@700&family=Roboto+Condensed:wght@400&display=swap">
<style>
  :root{
    --stage:#ffffff;
    --board:#0f0d0b;
    --board-warm:#1e1912;
    --gold:#c9a24a;
    --gold-light:#f0d58a;
    --teal:#1fb3a8;
    --crease:#d9d9d9;
    --window:#ffffff;
    --copy:#e6e0d4;
  }
  html,body{margin:0;padding:0;width:1194px;height:1200px;overflow:hidden;background:var(--stage);}
  .template{position:absolute;left:366px;top:20px;width:461px;height:1160px;display:block;}
  .script{font-family:"Kaushan Script",cursive;fill:var(--gold-light);}
  .serif{font-family:"Playfair Display",serif;font-weight:700;fill:var(--gold);}
  .brand{font-family:"Playfair Display",serif;font-weight:700;fill:var(--teal);}
  .copy{font-family:"Roboto Condensed",sans-serif;font-size:8.5px;fill:var(--copy);}
  .crease{fill:none;stroke:var(--crease);stroke-width:1;}
  .window{fill:var(--window);}
</style>
</head>
<body>
<svg class="template" viewBox="740 55 565 1420" xmlns="http://www.w3.org/2000/svg">
  <defs>
    <linearGradient id="boardFill" x1="0" y1="0" x2="0" y2="1">
      <stop offset="0" stop-color="var(--board-warm)"/>
      <stop offset="0.5" stop-color="var(--board)"/>
      <stop offset="1" stop-color="var(--board-warm)"/>
    </linearGradient>
    <radialGradient id="glowLow" cx="0.5" cy="0.5" r="0.5">
      <stop offset="0" stop-color="#d9a23a" stop-opacity="0.55"/>
      <stop offset="1" stop-color="#d9a23a" stop-opacity="0"/>
    </radialGradient>
    <radialGradient id="glowHigh" cx="0.5" cy="0.5" r="0.5">
      <stop offset="0" stop-color="#b89a3e" stop-opacity="0.35"/>
      <stop offset="1" stop-color="#b89a3e" stop-opacity="0"/>
    </radialGradient>
    <linearGradient id="photoTone" x1="0" y1="0" x2="1" y2="1">
      <stop offset="0" stop-color="#4a4540"/>
      <stop offset="0.6" stop-color="#2a2522"/>
      <stop offset="1" stop-color="#15110f"/>
    </linearGradient>
  </defs>

  <!-- die shape -->
  <path class="board" fill="url(#boardFill)" d="
    M817 68 H985 V205 L1003 205 L1045 205 V145 L1065 145 L1195 145 L1213 163 V205 L1255 205 L1275 245 V270 L1283 270
    V1448 H1245 L1225 1425 V1415 H1170 V1448 H1048 V1430 H985 V1460 H820 V1440 L800 1418 L762 1380 V285 L820 270 V68 Z"/>

  <!-- ambient glows -->
  <g role="img" aria-label="Soft gold light swirl decoration">
    <ellipse cx="900" cy="1100" rx="180" ry="220" fill="url(#glowLow)"/>
    <ellipse cx="1150" cy="1180" rx="170" ry="230" fill="url(#glowLow)"/>
    <ellipse cx="1160" cy="300" rx="140" ry="160" fill="url(#glowHigh)"/>
    <ellipse cx="920" cy="380" rx="120" ry="160" fill="url(#glowHigh)"/>
  </g>

  <!-- crease lines -->
  <g class="crease">
    <line x1="820" y1="270" x2="820" y2="1440"/>
    <line x1="985" y1="205" x2="985" y2="1430"/>
    <line x1="1048" y1="205" x2="1048" y2="1430"/>
    <line x1="1213" y1="205" x2="1213" y2="1415"/>
    <line x1="820" y1="270" x2="1283" y2="270"/>
    <line x1="820" y1="1395" x2="1283" y2="1395"/>
    <line x1="820" y1="100" x2="985" y2="100"/>
    <path d="M832 1395 L860 1418 H945 L975 1395"/>
    <path d="M1060 1395 V1418 H1100"/>
  </g>

  <!-- tuck flap holes -->
  <circle cx="902" cy="158" r="17" fill="none" stroke="var(--crease)" stroke-width="1.5"/>
  <circle cx="902" cy="215" r="17" fill="none" stroke="var(--crease)" stroke-width="1.5"/>

  <!-- top flap titles -->
  <text class="script" x="1131" y="229" font-size="19" text-anchor="middle">Graduation</text>
  <text class="serif" x="1131" y="256" font-size="24" text-anchor="middle">TASSEL</text>
  <text class="script" x="1131" y="297" font-size="19" text-anchor="middle">Graduation</text>
  <text class="serif" x="1131" y="324" font-size="24" text-anchor="middle">TASSEL</text>

  <!-- back panel title -->
  <g transform="translate(905 465) rotate(90)">
    <text class="script" x="0" y="-22" font-size="46" text-anchor="middle">Graduation</text>
    <text class="serif" x="0" y="32" font-size="60" text-anchor="middle">TASSEL</text>
  </g>

  <!-- photo area -->
  <rect x="821" y="600" width="160" height="360" fill="url(#photoTone)" role="img" aria-label="Photo of a graduate in cap and gown having her tassel turned"/>

  <!-- feature copy -->
  <g transform="translate(955 972) rotate(90)">
    <text class="copy" x="0" y="0">High quality poly academic regalia</text>
    <text class="copy" x="10" y="10">graduation tassel.</text>
    <text class="copy" x="0" y="28">Each tassel comes with 2018 year charm</text>
    <text class="copy" x="0" y="46">Free moving current year charm "signet"</text>
    <text class="copy" x="0" y="64">Reinforced metal clasp holder</text>
    <text class="copy" x="0" y="82">We are specialized in all kinds of gradua-</text>
    <text class="copy" x="0" y="92">tion garments and accessories.</text>
  </g>

  <!-- brand names -->
  <g transform="translate(905 1240) rotate(90)">
    <text class="brand" x="0" y="20" font-size="60" text-anchor="middle">CordaMax</text>
  </g>
  <g transform="translate(1135 1240) rotate(-90)">
    <text class="brand" x="0" y="20" font-size="60" text-anchor="middle">CordaMax</text>
  </g>

  <!-- display window -->
  <path class="window" d="M1101 365 A29 29 0 0 1 1159 365 V487 H1172 Q1182 487 1182 497 V530 Q1182 540 1172 540 H1159 V1078 H1101 V540 H1088 Q1077 540 1077 530 V497 Q1077 487 1088 487 H1101 Z"/>
</svg>
</body>
</html>
```